Cradlecraft by Lorna Business Card Design

i am starting a new business as a reborn artist (that is painting dolls to make them look like real live babies)

i eventually want to sell the dolls that i make and have classed in reborning. but at the moment i just want to get my name out there.

I do not currently have images of the dolls so cannot have an image in the design.

Non compulsory thoughts: i like the look of old wood, white and baby pink,even hot pink, and lace, denim. i had in mind something like a tiny baby in a old cradle or something, a old drawer, box, something different or unusual, it has to be a girl baby. i am also open to other thoughts on the matter. i would like plain writing not all swirly
Updates

Sorry to change but would like it to read country cradlecraft by lorna.

Industry/Entity Type

Painting

Contact Information for Business Card

Cradlecraft by Lorna
country babies that never grow up
Reborn Artist Lorna Whitby
0431 756 842
marlo.t@quillbox.com

```html
<!DOCTYPE html>
<html lang="en">
<head>
<meta charset="UTF-8">
<title>Cradlecraft by Lorna – Business Card</title>
<link href="https://fonts.googleapis.com/css2?family=Exo+2:wght@400;500&display=swap" rel="stylesheet">
<style>
  :root {
    --backdrop: #2f86bb;
    --lace-blue: #3a8fc6;
    --lace-pink: #ec5fa6;
    --wood-light: #eeeeee;
    --wood-mid: #d9d9d9;
    --wood-dark: #c4c4c4;
    --divider-pink: #f06aa8;
    --ink: #141414;
    --icon-ink: #1a1a1a;
  }
  * { box-sizing: border-box; margin: 0; padding: 0; }
  html, body {
    width: 1200px;
    height: 900px;
    overflow: hidden;
  }
  body {
    background: var(--backdrop);
    display: flex;
    align-items: center;
    justify-content: center;
    font-family: "Exo 2", "Segoe UI", sans-serif;
  }
  .business-card {
    position: relative;
    width: 900px;
    height: 514px;
    box-shadow: 0 18px 40px rgba(0, 0, 0, 0.25);
    overflow: hidden;
  }
  .wood-surface {
    position: absolute;
    inset: 0;
    background: linear-gradient(160deg, var(--wood-light) 0%, var(--wood-mid) 50%, var(--wood-light) 100%);
  }
  .lace-band {
    position: absolute;
    left: 0;
    width: 100%;
    height: 66px;
    background: linear-gradient(90deg, var(--lace-blue) 0%, var(--lace-pink) 50%, var(--lace-blue) 100%);
  }
  .lace-band--top { top: 0; }
  .lace-band--bottom { bottom: 0; }
  .brand-name {
    position: absolute;
    left: 40px;
    top: 202px;
    width: 370px;
    text-align: center;
    white-space: nowrap;
    color: var(--ink);
    font-weight: 500;
    font-size: 34px;
    line-height: 1.2;
  }
  .section-divider {
    position: absolute;
    left: 440px;
    top: 120px;
    width: 2px;
    height: 210px;
    background: var(--divider-pink);
  }
  .contact-block {
    position: absolute;
    left: 490px;
    top: 128px;
    color: var(--ink);
  }
  .contact-name {
    font-size: 28px;
    font-weight: 500;
    letter-spacing: 1px;
    text-transform: uppercase;
    line-height: 1.1;
  }
  .contact-role {
    font-size: 24px;
    font-weight: 400;
    line-height: 1.2;
    margin-bottom: 14px;
  }
  .contact-line {
    display: flex;
    align-items: center;
    gap: 10px;
    font-size: 20px;
    line-height: 1.6;
  }
  .contact-icon { width: 18px; height: 18px; flex: none; }
  .tagline {
    position: absolute;
    left: 430px;
    bottom: 92px;
    font-size: 27px;
    font-weight: 400;
    color: var(--ink);
  }
</style>
</head>
<body>
  <div class="business-card">
    <div class="wood-surface" role="img" aria-label="Whitewashed weathered wooden planks background"></div>
    <div class="lace-band lace-band--top" role="img" aria-label="Pink floral lace trim on blue denim"></div>
    <div class="lace-band lace-band--bottom" role="img" aria-label="Pink floral lace trim on blue denim"></div>

    <h1 class="brand-name">Cradlecraft by Lorna</h1>

    <div class="section-divider"></div>

    <div class="contact-block">
      <p class="contact-name">Lorna Whitby</p>
      <p class="contact-role">Reborn Artist</p>
      <p class="contact-line">
        <svg class="contact-icon" viewBox="0 0 20 20" aria-hidden="true">
          <circle cx="10" cy="10" r="10" fill="var(--icon-ink)"/>
          <path d="M7 5.5c.5-.4 1.1-.3 1.4.2l.9 1.6c.2.4.1.9-.2 1.2l-.6.5c.5 1.1 1.3 1.9 2.4 2.4l.5-.6c.3-.3.8-.4 1.2-.2l1.6.9c.5.3.6.9.2 1.4l-.6.7c-.5.6-1.4.8-2.1.4-2.3-1.1-4.1-2.9-5.2-5.2-.4-.7-.2-1.6.4-2.1z" fill="#fff"/>
        </svg>
        0431 756 842
      </p>
      <p class="contact-line">
        <svg class="contact-icon" viewBox="0 0 20 20" aria-hidden="true">
          <circle cx="10" cy="10" r="10" fill="var(--icon-ink)"/>
          <rect x="5" y="6.5" width="10" height="7" rx="1" fill="#fff"/>
          <path d="M5.5 7l4.5 3.5L14.5 7" fill="none" stroke="var(--icon-ink)" stroke-width="1"/>
        </svg>
        marlo.t@quillbox.com
      </p>
    </div>

    <p class="tagline">Babies that never grow up</p>
  </div>
</body>
</html>
```